Velvetmoth chocolates label & packaging design

We make high end chocolates .Enrobed medjoul dates ,truffles and filled chocolates . We have to upgrade our packaging to reflect the quality of the products
1 . Chocolate box label or sleeve for
1a truffle box
2a enrobed date box
3a Chocolate box
4a Mixed chocolate truffle and date box .
I also have a project in mind to make hot chocolate kits which would be our hot chocolate powder chocolate & home made marshmallows.
The images attached should give an idea of the products The label designs included are an example of the colour palette we like .
We would like to include the velvetmoth logo as part of the design .
Our chocolates are made without adding. Dairy or refined sugars and using the best ingredients available .

Target Market(s)

Food lovers, those who prioritise quality above quantity .

Industry/Entity Type

Chocolatier

Font styles to use
Script

Colors
0054AA
0677BA
7BADD7
CADEEF
E8F1F8
F0912C
F2A743
F7CA91
FBE8D2
FDF5EE
E54698
E96AAD
F1A4CE
F9D9EA
FCEFF6

Requirements
Must have
• An element of luxury
Nice to have
• Something to reflect the integrity of the ingredients and the love that goes into making the chocolates.
Should not have
• Too much packaging

```html
<!DOCTYPE html>
<html lang="en">
<head>
<meta charset="utf-8">
<title>Velvetmoth Chocolates – Box Labels</title>
<link rel="stylesheet" href="https://fonts.googleapis.com/css2?family=Poiret+One&family=Caveat:wght@400;500&family=Josefin+Sans:wght@400;600&display=swap">
<style>
  :root {
    --backdrop: #c8bcaa;
    --orange: #ee8f2a;
    --pink: #dc3f90;
    --slate: #4d6276;
    --mist: #c7d5e0;
    --cream: #f6ede4;
    --blush: #f9e4ee;
    --ink: #26181a;
    --navy: #2f3d5c;
    --plum: #3b1e36;
    --white: #fdf5ee;
  }
  * { box-sizing: border-box; margin: 0; padding: 0; }
  html, body { width: 1200px; height: 819px; overflow: hidden; }
  body { background: var(--backdrop); position: relative; font-family: "Josefin Sans", sans-serif; }

  .label { position: absolute; top: 60px; width: 400px; height: 700px; }
  .label--truffle { left: 170px; }
  .label--chocolate { left: 630px; }

  .side-band { position: absolute; top: 0; width: 52px; height: 100%; }
  .side-band--left { left: 0; }
  .side-band--right { right: 0; }
  .label--truffle .side-band { background: var(--slate); }
  .label--chocolate .side-band { background: var(--mist); }
  .side-band__stripe { position: absolute; top: 78px; left: 0; width: 100%; height: 30px; }
  .label--truffle .side-band__stripe { background: var(--cream); }
  .label--chocolate .side-band__stripe { background: var(--blush); }

  .panel { position: absolute; left: 52px; top: 0; width: 296px; height: 100%; text-align: center; }
  .label--truffle .panel { background: var(--orange); }
  .label--chocolate .panel { background: var(--pink); }

  .product-shot { position: absolute; left: 50%; top: 14px; transform: translateX(-50%); width: 110px; height: 78px; border-radius: 46% 46% 40% 40%; }
  .label--truffle .product-shot { background: radial-gradient(circle at 45% 40%, #4a3a35, #1e1614); }
  .label--chocolate .product-shot { border-radius: 6px; width: 80px; height: 84px; background: linear-gradient(160deg, #8a5638, #4a2616); }

  .kicker { position: absolute; top: 110px; width: 100%; font-family: "Caveat", cursive; font-size: 24px; color: var(--white); }
  .title { position: absolute; top: 138px; width: 100%; font-family: "Poiret One", sans-serif; font-size: 50px; letter-spacing: 1px; }
  .label--truffle .title { color: var(--ink); }
  .label--chocolate .title { color: var(--plum); font-size: 44px; top: 144px; }
  .tagline { position: absolute; width: 100%; font-family: "Caveat", cursive; font-size: 21px; }
  .tagline--top { top: 205px; color: var(--white); opacity: .9; }
  .tagline--low { top: 500px; }
  .label--truffle .tagline--low { color: var(--navy); }
  .label--chocolate .tagline--low { color: var(--plum); }

  .brand-frame { position: absolute; left: 28px; top: 258px; width: 240px; height: 222px; border: 2px solid var(--ink); display: flex; flex-direction: column; align-items: center; justify-content: center; gap: 14px; }
  .label--chocolate .brand-frame { border-color: var(--plum); }
  .brand-name { font-family: "Poiret One", sans-serif; font-size: 42px; line-height: 1; color: var(--navy); }
  .label--chocolate .brand-name { color: var(--plum); }
  .brand-line { font-family: "Josefin Sans", sans-serif; font-weight: 600; font-size: 19px; letter-spacing: 3px; color: var(--navy); }
  .label--chocolate .brand-line { color: var(--plum); }

  .footnote { position: absolute; top: 612px; width: 100%; font-family: "Caveat", cursive; font-size: 20px; }
  .label--truffle .footnote { color: var(--navy); }
  .label--chocolate .footnote { color: var(--plum); }

  .zigzag { position: absolute; left: 0; bottom: 0; width: 100%; height: 12px; display: block; }
</style>
</head>
<body>

  <section class="label label--truffle">
    <div class="side-band side-band--left"><span class="side-band__stripe"></span></div>
    <div class="side-band side-band--right"><span class="side-band__stripe"></span></div>
    <div class="panel">
      <div class="product-shot" role="img" aria-label="Photo of a dark chocolate truffle"></div>
      <p class="kicker">chocolate</p>
      <h2 class="title">TRUFFLE</h2>
      <p class="tagline tagline--top">the best ingredients available</p>
      <div class="brand-frame">
        <span class="brand-name">velvetmoth</span>
        <span class="brand-line">CHOCOLATES</span>
      </div>
      <p class="tagline tagline--low">the best ingredients available</p>
      <p class="footnote">our chocolates are made without adding</p>
      <svg class="zigzag" viewBox="0 0 296 12" preserveAspectRatio="none" aria-hidden="true">
        <polygon fill="#c8bcaa" points="0,12 0,6 8,0 16,6 24,0 32,6 40,0 48,6 56,0 64,6 72,0 80,6 88,0 96,6 104,0 112,6 120,0 128,6 136,0 144,6 152,0 160,6 168,0 176,6 184,0 192,6 200,0 208,6 216,0 224,6 232,0 240,6 248,0 256,6 264,0 272,6 280,0 288,6 296,0 296,12"/>
      </svg>
    </div>
  </section>

  <section class="label label--chocolate">
    <div class="side-band side-band--left"><span class="side-band__stripe"></span></div>
    <div class="side-band side-band--right"><span class="side-band__stripe"></span></div>
    <div class="panel">
      <div class="product-shot" role="img" aria-label="Photo of stacked milk chocolate pieces"></div>
      <p class="kicker">chocolate</p>
      <h2 class="title">CHOCOLATE</h2>
      <p class="tagline tagline--top">the best ingredients available</p>
      <div class="brand-frame">
        <span class="brand-name">velvetmoth</span>
        <span class="brand-line">CHOCOLATES</span>
      </div>
      <p class="tagline tagline--low">the best ingredients available</p>
      <p class="footnote">our chocolates are made without adding</p>
      <svg class="zigzag" viewBox="0 0 296 12" preserveAspectRatio="none" aria-hidden="true">
        <polygon fill="#c8bcaa" points="0,12 0,6 8,0 16,6 24,0 32,6 40,0 48,6 56,0 64,6 72,0 80,6 88,0 96,6 104,0 112,6 120,0 128,6 136,0 144,6 152,0 160,6 168,0 176,6 184,0 192,6 200,0 208,6 216,0 224,6 232,0 240,6 248,0 256,6 264,0 272,6 280,0 288,6 296,0 296,12"/>
      </svg>
    </div>
  </section>

</body>
</html>
```